Hochzeitseinladung
Zielgruppe
Gastronomie - Zielgruppe ist ein Hochzeitspaar, welches bei uns feiert. Wir dürfen Ihre Hochzeitseinladung entwerfen.
Aufgabenstellung
Den Textvorschlag des Brautpaares findet Ihr im Anhang. Das Thema der Hochzeit ist AMORE.
1. Die Hochzeitseinladung darf gerne kreativ gestaltet sein, vielleicht in Form des Moodboard-Bildes im Anhang? Mattes hat braune Haare und Locken und Doreen lange braune Haare. Beide tragen eine Brille.
Das Hochzeitspaar hat noch einen kleinen braunen Zwergpudel 'Fips', vielleicht findet er auch noch Platz auf der Einladungskarte ;-).
2. Als Alternativ-Vorschlag wäre ein klassisches Design auf zB geprägtem Papier toll.
3. Etwas Schlichtes mit einem Neon-Accessoire würde das Hochzeitspaar auch gut finden. Zb brauner Karton mit einem Neonband.

```html
<!DOCTYPE html>
<html lang="de">
<head>
<meta charset="utf-8">
<title>Details – Zeitplan für unsere Hochzeit</title>
<link href="https://fonts.googleapis.com/css2?family=Allura&family=Cormorant+Garamond:wght@400;500&display=swap" rel="stylesheet">
<style>
  :root {
    --paper: #f8f6f1;
    --ink: #6a645e;
    --ink-dark: #2f2d2b;
    --gold: #c9a75c;
    --blush: #e9d8cc;
    --blush-deep: #d9c2b3;
    --sage: #a9b79b;
    --leaf: #7f9560;
  }
  * { margin: 0; padding: 0; box-sizing: border-box; }
  html, body { width: 879px; height: 1200px; overflow: hidden; background: var(--paper); }
  .card {
    position: relative;
    width: 879px; height: 1200px;
    background: var(--paper);
    font-family: "Cormorant Garamond", Georgia, serif;
    color: var(--ink);
  }
  .decor { position: absolute; }
  .floral-top-left {
    left: 0; top: 0; width: 210px; height: 370px;
    background:
      radial-gradient(ellipse 90px 80px at 70px 110px, var(--blush) 0%, rgba(233,216,204,0) 100%),
      radial-gradient(ellipse 70px 60px at 150px 60px, var(--blush-deep) 0%, rgba(217,194,179,0) 100%),
      radial-gradient(ellipse 60px 140px at 60px 260px, rgba(169,183,155,.55) 0%, rgba(169,183,155,0) 100%);
  }
  .floral-top-right {
    right: 0; top: 0; width: 250px; height: 370px;
    background:
      radial-gradient(ellipse 100px 90px at 170px 110px, var(--blush) 0%, rgba(233,216,204,0) 100%),
      radial-gradient(ellipse 70px 60px at 90px 70px, var(--blush-deep) 0%, rgba(217,194,179,0) 100%),
      radial-gradient(ellipse 70px 140px at 180px 260px, rgba(169,183,155,.55) 0%, rgba(169,183,155,0) 100%);
  }
  .leaves-bottom-left {
    left: 0; bottom: 0; width: 165px; height: 245px;
    background: radial-gradient(ellipse 80px 120px at 70px 140px, rgba(127,149,96,.6) 0%, rgba(127,149,96,0) 100%);
  }
  .leaves-bottom-right {
    right: 0; bottom: 0; width: 170px; height: 245px;
    background: radial-gradient(ellipse 80px 120px at 100px 140px, rgba(127,149,96,.6) 0%, rgba(127,149,96,0) 100%);
  }

  .title {
    position: absolute; left: 0; width: 100%; top: 135px;
    text-align: center;
    font-family: "Allura", cursive;
    font-size: 150px; line-height: 1;
    color: var(--gold);
  }
  .subtitle {
    position: absolute; left: 0; width: 100%; top: 326px;
    text-align: center;
    font-size: 21px; letter-spacing: .5px;
    text-transform: uppercase;
  }

  .timeline { position: absolute; left: 0; top: 440px; width: 100%; height: 240px; }
  .timeline-line { position: absolute; left: 166px; top: 97px; width: 529px; height: 2px; background: var(--ink-dark); }
  .step { position: absolute; width: 170px; margin-left: -85px; text-align: center; top: 0; }
  .step-icon { display: block; margin: 0 auto; width: 80px; height: 80px; }
  .step-dot { width: 18px; height: 18px; border-radius: 50%; background: var(--ink-dark); margin: 9px auto 0; }
  .step-time { margin-top: 10px; font-size: 22px; font-weight: 500; line-height: 1; }
  .step-label { margin-top: 5px; font-size: 16px; line-height: 21px; text-transform: uppercase; letter-spacing: .3px; }

  .section-heading {
    position: absolute; left: 0; width: 100%;
    text-align: center;
    font-family: "Allura", cursive;
    font-size: 60px; line-height: 1;
    color: var(--gold);
  }
  .section-heading.civil { top: 735px; }
  .section-heading.dress { top: 962px; }
  .section-text {
    position: absolute; left: 70px; width: 739px;
    text-align: center;
    font-size: 21px; line-height: 29.5px;
  }
  .section-text.civil { top: 798px; }
  .section-text.dress { top: 1030px; }
</style>
</head>
<body>
<main class="card">
  <div class="decor floral-top-left" role="img" aria-label="Aquarell-Blüten in Altrosa mit Salbeiblättern"></div>
  <div class="decor floral-top-right" role="img" aria-label="Aquarell-Blüten in Altrosa mit Salbeiblättern"></div>
  <div class="decor leaves-bottom-left" role="img" aria-label="Grüne Aquarell-Blattzweige"></div>
  <div class="decor leaves-bottom-right" role="img" aria-label="Grüne Aquarell-Blattzweige"></div>

  <h1 class="title">Details</h1>
  <p class="subtitle">Zeitplan für unsere Hochzeit</p>

  <section class="timeline">
    <div class="timeline-line"></div>

    <div class="step" style="left:166px">
      <svg class="step-icon" viewBox="0 0 80 80" fill="none" stroke="#555" stroke-width="1.6">
        <path d="M30 8v8M27 11h6M24 30l6-12 6 12M24 30v42M36 30v42M24 44h12l0 0M36 46l10-8h18l6 8v26H36M8 72h66M28 72V62h4v10M44 56h4v6h-4zM52 56h4v6h-4zM60 56h4v6h-4z"/>
      </svg>
      <div class="step-dot"></div>
      <div class="step-time">13:30 Uhr</div>
      <div class="step-label">Standesamt<br>Lindenhof<br>Kloster</div>
    </div>

    <div class="step" style="left:342px">
      <svg class="step-icon" viewBox="0 0 80 80" fill="none" stroke="#555" stroke-width="1.6">
        <path d="M22 24l14 4-4 16c-2 5-8 6-11 2zM27 46l-6 20M15 67l12 2"/>
        <path d="M58 24l-14 4 4 16c2 5 8 6 11 2zM53 46l6 20M65 67l-12 2"/>
        <path d="M40 16c-2-3-6-1-4 2l4 4 4-4c2-3-2-5-4-2z"/>
        <path d="M12 36h4M14 44h4M64 36h4M62 44h4"/>
      </svg>
      <div class="step-dot"></div>
      <div class="step-time">14:30 UHR</div>
      <div class="step-label">Sektempfang<br>Salon Perle</div>
    </div>

    <div class="step" style="left:519px">
      <svg class="step-icon" viewBox="0 0 80 80" fill="none" stroke="#333" stroke-width="2">
        <path d="M40 48A26 26 0 1 1 48 18"/>
        <path d="M30 20v16h10"/>
        <path d="M38 44h30v14c0 8-6 14-14 14h-2c-8 0-14-6-14-14z"/>
        <path d="M68 48h4c3 0 3 10 0 10h-4"/>
        <path d="M48 36c-3-4 3-6 0-10M56 36c-3-4 3-6 0-10M64 36c-3-4 3-6 0-10"/>
      </svg>
      <div class="step-dot"></div>
      <div class="step-time">AB 16:00 UHR</div>
      <div class="step-label">Kurze Pause</div>
    </div>

    <div class="step" style="left:695px">
      <svg class="step-icon" viewBox="0 0 80 80" fill="none" stroke="#333" stroke-width="1.8">
        <circle cx="40" cy="42" r="20"/>
        <circle cx="40" cy="42" r="13"/>
        <path d="M12 18c-5 0-5 14 0 14s5-14 0-14zM12 32v36"/>
        <path d="M64 18v12c0 3 2 4 4 4s4-1 4-4V18M68 18v50M68 34v34"/>
      </svg>
      <div class="step-dot"></div>
      <div class="step-time">18:30UHR</div>
      <div class="step-label">Einfinden im<br>Gasthaus<br>Alter<br>Brunnen</div>
    </div>
  </section>

  <h2 class="section-heading civil">Standesamt</h2>
  <p class="section-text civil">Im Standesamt stehen leider nur 20 Plätze zur Verfügung. Falls Ihr Interesse habt, freue ich mich über Eure Nachricht, damit wir gemeinsam eine Lösung finden können.</p>

  <h2 class="section-heading dress">Dresscodes</h2>
  <p class="section-text dress">Tagsüber : Cocktail<br>Abends: Festlich elegant &amp; dunkler Anzug</p>
</main>
</body>
</html>
```